e-Book Cover Design Project

I need an e-book cover design for a book called The Quiet Orchard. A handbook for hearts (turned sour). It is non-fiction. It has an apple theme throughout so I would like to see designs that use a red apple (perhaps even a bite out of it), simple text and simple background. Despite the theme, the final design should still be positive.

Target Market(s)

Most likely women aged 25 and over.

Requirements
Must have
• real red apple
Nice to have
• cupids arrow
Should not have
• cartoons

```html
<!DOCTYPE html>
<html lang="en">
<head>
<meta charset="utf-8">
<title>The Quiet Orchard – eBook Cover</title>
<link rel="stylesheet" href="https://fonts.googleapis.com/css2?family=Arvo:wght@700&family=Mulish:wght@400;500&display=swap">
<style>
  :root {
    --page: #fdfdee;
    --ink: #231a15;
    --sky-deep: #2cc3d3;
    --sky-mid: #7fd8df;
    --sky-light: #e9f4e4;
    --apple-red: #d6141a;
    --apple-dark: #8e0a0c;
    --apple-light: #f24a3c;
  }
  * { margin: 0; padding: 0; box-sizing: border-box; }
  html, body {
    width: 1200px;
    height: 900px;
    overflow: hidden;
    background: var(--page);
  }
  .canvas {
    position: relative;
    width: 1200px;
    height: 900px;
    background: var(--page);
  }
  .cover {
    position: absolute;
    left: 305px;
    top: 18px;
    width: 585px;
    height: 854px;
    overflow: hidden;
    box-shadow: 0 8px 18px rgba(80, 60, 30, 0.35);
  }
  .cover__sky {
    position: absolute;
    inset: 0;
    background:
      radial-gradient(ellipse 70% 35% at 30% 15%, rgba(233,244,228,0.7), transparent 70%),
      radial-gradient(ellipse 60% 30% at 75% 55%, rgba(233,244,228,0.6), transparent 70%),
      radial-gradient(ellipse 90% 40% at 50% 92%, rgba(240,246,226,0.9), transparent 70%),
      linear-gradient(180deg, var(--sky-deep) 0%, var(--sky-mid) 45%, var(--sky-light) 85%, var(--sky-mid) 100%);
  }
  .cover__title {
    position: absolute;
    left: 0;
    right: 0;
    top: 28px;
    text-align: center;
    font-family: "Arvo", serif;
    font-weight: 700;
    color: var(--ink);
    text-transform: uppercase;
    line-height: 0.92;
  }
  .cover__title span { display: block; }
  .title--small { font-size: 104px; }
  .title--mid { font-size: 128px; letter-spacing: 2px; }
  .title--wide { font-size: 104px; letter-spacing: -2px; }
  .cover__apple {
    position: absolute;
    left: 168px;
    top: 360px;
    width: 268px;
    height: 300px;
    border-radius: 48% 48% 44% 44% / 40% 40% 58% 58%;
    background: radial-gradient(ellipse 60% 55% at 40% 35%, var(--apple-light), var(--apple-red) 55%, var(--apple-dark) 100%);
    box-shadow: 0 14px 10px -8px rgba(40, 30, 20, 0.35);
  }
  .cover__subtitle {
    position: absolute;
    left: 0;
    right: 0;
    top: 676px;
    text-align: center;
    font-family: "Mulish", sans-serif;
    font-weight: 500;
    font-size: 36px;
    line-height: 1.2;
    color: var(--ink);
    text-transform: uppercase;
  }
  .cover__author {
    position: absolute;
    left: 0;
    right: 0;
    top: 788px;
    text-align: center;
    font-family: "Mulish", sans-serif;
    font-weight: 400;
    font-size: 28px;
    letter-spacing: 1px;
    color: var(--ink);
  }
</style>
</head>
<body>
  <div class="canvas">
    <div class="cover">
      <div class="cover__sky" role="img" aria-label="Soft turquoise sky with pale clouds"></div>
      <h1 class="cover__title">
        <span class="title--small">The</span>
        <span class="title--mid">Quiet</span>
        <span class="title--wide">Orchard</span>
      </h1>
      <div class="cover__apple" role="img" aria-label="Photograph of a shiny red apple with a leaf and a heart-shaped bite"></div>
      <p class="cover__subtitle">A handbook for hearts<br>(turned sour)</p>
      <p class="cover__author">Maren Ellison</p>
    </div>
  </div>
</body>
</html>
```